Lantern Stewardship Frame

I am looking for a graphic design of the attached leadership model. The colors and design can be altered in any manner that brings the model alive version of the house model.

```html
<!DOCTYPE html>
<html lang="en">
<head>
<meta charset="utf-8">
<title>Lantern Stewardship Frame</title>
<link href="https://fonts.googleapis.com/css2?family=Oswald:wght@500;600&family=Montserrat:wght@700;800&family=Open+Sans:wght@400;700&display=swap" rel="stylesheet">
<style>
  :root {
    --slate: #4a4a4c;
    --map: #e6e6e6;
    --navy: #0a2f9c;
    --yellow: #ffcb2b;
    --yellow-fold: #8a7440;
    --plum: #a8508a;
    --paper: #ffffff;
    --olive: #5e8a12;
    --cyan: #00c8ff;
    --cyan-fold: #066f8c;
    --leaf: #009a3a;
    --leaf-fold: #0b5a26;
    --coral: #ff6633;
    --coral-fold: #8f2a10;
    --ink: #1f1f1f;
  }
  * { box-sizing: border-box; margin: 0; padding: 0; }
  html, body { width: 825px; height: 1200px; overflow: hidden; background: #fff; }
  .poster { position: relative; width: 825px; height: 1200px; background: #fff; font-family: 'Open Sans', sans-serif; }
  .spine { position: absolute; left: 0; top: 0; width: 134px; height: 1166px; background: var(--slate); }
  .world { position: absolute; left: 270px; top: 22px; width: 530px; height: 280px;
    background: radial-gradient(ellipse at 55% 45%, var(--map) 0%, rgba(230,230,230,0.6) 55%, rgba(255,255,255,0) 75%); }
  .title { position: absolute; left: 161px; top: 168px; font-family: 'Oswald', sans-serif; font-weight: 600;
    font-size: 46px; letter-spacing: 22px; color: var(--navy); line-height: 1; }
  .tagline { position: absolute; left: 161px; top: 234px; width: 620px; font-family: 'Montserrat', sans-serif;
    font-weight: 800; font-size: 21px; line-height: 27px; color: var(--slate); }
  .col { position: absolute; top: 369px; height: 797px; }
  .col-org { left: 134px; width: 222px; background: var(--plum); }
  .col-inter { left: 356px; width: 222px; background: var(--paper); box-shadow: 6px 0 8px -4px rgba(0,0,0,0.15); }
  .col-personal { left: 578px; width: 247px; background: var(--olive); }
  .banner { position: absolute; left: 85px; width: 632px; height: 64px; background: var(--yellow);
    border-top-right-radius: 48px; box-shadow: 0 3px 4px rgba(0,0,0,0.15); display: flex; align-items: center; }
  .banner h2 { font-family: 'Montserrat', sans-serif; font-weight: 800; font-size: 27px; color: var(--slate); letter-spacing: 1px; }
  .banner-outer { top: 305px; }
  .banner-outer h2 { margin-left: 84px; }
  .banner-inner { top: 952px; }
  .banner-inner h2 { margin-left: 78px; letter-spacing: 2px; }
  .banner svg { position: absolute; left: 18px; top: 8px; }
  .fold { position: absolute; }
  .icon { position: absolute; top: 390px; }
  .level { position: absolute; top: 463px; width: 189px; height: 64px; border-top-right-radius: 44px;
    font-family: 'Oswald', sans-serif; font-weight: 500; font-size: 24px; line-height: 25px; padding: 8px 0 0 14px; }
  .level-org { left: 85px; background: var(--cyan); color: var(--navy); }
  .level-inter { left: 307px; background: var(--leaf); color: #fff; }
  .level-personal { left: 528px; background: var(--coral); color: #fff; }
  .block { position: absolute; }
  .block h3 { font-weight: 700; font-size: 16.5px; line-height: 20px; margin-bottom: -2px; }
  .points { list-style: none; font-size: 16.5px; line-height: 31px; white-space: nowrap; }
  .points li { position: relative; padding-left: 27px; }
  .points li + li { margin-top: -7px; }
  .points li::before { content: ""; position: absolute; left: 0; top: 12.5px; width: 6px; height: 6px; border-radius: 50%; background: currentColor; }
  .on-plum { color: #fff; }
  .on-paper { color: var(--ink); }
  .on-paper h3 { color: var(--leaf); }
  .on-paper .points li::before { background: var(--leaf); }
  .on-olive { color: #fff; }
  .link-arrow { position: absolute; top: 646px; }
</style>
</head>
<body>
<div class="poster">
  <div class="spine"></div>
  <div class="world" role="img" aria-label="Faint grey world map"></div>

  <h1 class="title">LANTERN</h1>
  <p class="tagline">FOSTER CONTAGIOUS SUCCESS THROUGH PEOPLE, RELATIONSHIPS AND A SHARED VISION</p>

  <div class="col col-org"></div>
  <div class="col col-inter"></div>
  <div class="col col-personal"></div>

  <svg class="fold" style="left:85px;top:369px" width="49" height="26"><polygon points="0,0 49,0 49,26" fill="var(--yellow-fold)"/></svg>
  <div class="banner banner-outer">
    <svg width="48" height="48" viewBox="0 0 48 48" fill="var(--slate)" stroke="var(--slate)" stroke-width="3">
      <rect x="2" y="2" width="8" height="8" stroke="none"/><circle cx="10" cy="16" r="5" stroke="none"/>
      <path d="M36 4l6 6M42 4l-6 6M18 30l6 6M24 30l-6 6" fill="none"/>
      <path d="M22 14h10a6 6 0 0 1 6 6v16" fill="none"/><polygon points="22,9 16,14 22,19" stroke="none"/>
      <circle cx="38" cy="40" r="6" stroke="none"/>
    </svg>
    <h2>OUTER (IMPACT) STRATEGIES</h2>
  </div>

  <svg class="icon" style="left:145px" width="60" height="60" viewBox="0 0 60 60" fill="#fff">
    <circle cx="12" cy="8" r="6"/><path d="M1 24a11 9 0 0 1 22 0z"/>
    <circle cx="48" cy="8" r="6"/><path d="M37 24a11 9 0 0 1 22 0z"/>
    <circle cx="30" cy="38" r="6"/><path d="M19 56a11 9 0 0 1 22 0z"/>
    <path d="M22 12a14 14 0 0 1 16 0M10 32a20 20 0 0 0 6 16M50 32a20 20 0 0 1-6 16" fill="none" stroke="#fff" stroke-width="3"/>
  </svg>
  <svg class="icon" style="left:373px" width="64" height="60" viewBox="0 0 64 60" fill="#000">
    <circle cx="32" cy="18" r="12"/>
    <g stroke="#000" stroke-width="6"><path d="M32 2v32M16 18h32M21 7l22 22M43 7L21 29"/></g>
    <circle cx="32" cy="18" r="5" fill="#fff"/>
    <circle cx="13" cy="40" r="6"/><path d="M2 58a11 10 0 0 1 22 0z"/>
    <circle cx="51" cy="40" r="6"/><path d="M40 58a11 10 0 0 1 22 0z"/>
  </svg>
  <svg class="icon" style="left:593px" width="54" height="62" viewBox="0 0 54 62" fill="none" stroke="#fff" stroke-width="3.5">
    <circle cx="27" cy="8" r="5"/><path d="M10 2v8a8 8 0 0 0 8 8h18a8 8 0 0 0 8-8V2M20 18v8M34 18v8"/>
    <circle cx="27" cy="43" r="13"/>
    <polygon points="27,35 29.5,40.5 35,41 31,45 32,50.5 27,48 22,50.5 23,45 19,41 24.5,40.5" stroke-width="2"/>
    <path d="M2 43h5M47 43h5M7 30l4 3M47 30l-4 3M7 56l4-3M47 56l-4-3"/>
  </svg>

  <svg class="fold" style="left:85px;top:527px" width="49" height="26"><polygon points="0,0 49,0 49,26" fill="var(--cyan-fold)"/></svg>
  <svg class="fold" style="left:307px;top:527px" width="49" height="26"><polygon points="0,0 49,0 49,26" fill="var(--leaf-fold)"/></svg>
  <svg class="fold" style="left:528px;top:527px" width="50" height="26"><polygon points="0,0 50,0 50,26" fill="var(--coral-fold)"/></svg>
  <div class="level level-org">ORGANIZATION<br>LEVEL</div>
  <div class="level level-inter">INTERPERSONAL<br>LEVEL</div>
  <div class="level level-personal">PERSONAL<br>LEVEL</div>

  <div class="block on-plum" style="left:148px;top:543px;width:206px">
    <h3>WINS THEORY</h3>
    <ul class="points">
      <li>Develop concrete<br>outcomes, and<br>visible results</li>
      <li>Foster in-depth<br>changes, and new<br>practices</li>
      <li>Have a micro,<br>interpersonal or<br>local impact</li>
      <li>Cultivate positive<br>judgement, and<br>shared ambition</li>
    </ul>
  </div>
  <div class="block on-paper" style="left:370px;top:543px;width:206px">
    <h3>HEART LISTENING</h3>
    <ul class="points">
      <li>Ask open-ended<br>questions</li>
      <li>Affirm someone’s<br>strengths, efforts<br>and past success</li>
      <li>Reflect back what<br>is shared for<br>confirmation</li>
      <li>Summarize key<br>points to gain<br>insights</li>
      <li>Share and develop<br>mutual expertise</li>
    </ul>
  </div>
  <div class="block on-olive" style="left:599px;top:543px;width:222px">
    <h3>INSIGHT DIALOGUE</h3>
    <ul class="points">
      <li>Pause</li>
      <li>Relax</li>
      <li>Open</li>
      <li>Attune to<br>Emergence</li>
      <li>Listen Deeply</li>
      <li>Speak the Truth</li>
    </ul>
  </div>

  <svg class="link-arrow" style="left:332px" width="40" height="40" viewBox="0 0 42 42">
    <circle cx="21" cy="21" r="19" fill="var(--slate)" stroke="#fff" stroke-width="2.5"/>
    <path d="M22 10L11 21l11 11v-6h10v-10H22z" fill="#fff"/>
  </svg>
  <svg class="link-arrow" style="left:555px" width="40" height="40" viewBox="0 0 42 42">
    <circle cx="21" cy="21" r="19" fill="var(--slate)" stroke="#fff" stroke-width="2.5"/>
    <path d="M22 10L11 21l11 11v-6h10v-10H22z" fill="#fff"/>
  </svg>

  <svg class="fold" style="left:85px;top:1016px" width="49" height="26"><polygon points="0,0 49,0 49,26" fill="var(--yellow-fold)"/></svg>
  <div class="banner banner-inner">
    <svg width="48" height="48" viewBox="0 0 48 48" fill="var(--slate)" stroke="var(--slate)" stroke-width="3">
      <path d="M4 4l6 6M10 4l-6 6M18 26l6 6M24 26l-6 6" fill="none"/>
      <rect x="38" y="2" width="8" height="8" stroke="none"/><circle cx="36" cy="16" r="5" stroke="none"/>
      <path d="M28 16h-8a6 6 0 0 0-6 6v14" fill="none"/><polygon points="28,11 34,16 28,21" stroke="none"/>
      <circle cx="12" cy="40" r="6" stroke="none"/>
    </svg>
    <h2>INNER (WELLBEING) STRATEGIES</h2>
  </div>

  <ul class="points on-plum" style="position:absolute;left:148px;top:1044px;width:206px">
    <li>Physical Fitness</li>
    <li>Nutrition</li>
  </ul>
  <ul class="points on-paper" style="position:absolute;left:370px;top:1044px;width:206px">
    <li>Heart Rate<br>Variability</li>
    <li>Neurofeedback</li>
  </ul>
  <ul class="points on-olive" style="position:absolute;left:599px;top:1042px;width:222px">
    <li>Coastal Ramblers Club</li>
    <li>Video Gaming Club</li>
  </ul>
</div>
</body>
</html>
```